Design Large Inspirational Artwork with Long Quote

Design a large piece of art with a quote from Marcus Tillwright.

QUOTE
"The thing that's so interesting about being alive is that you're all in. No matter what you do, you're all in. This is gonna kill you, so I think you might as well play the most magnificent game you can while you're waiting. Because, do you have anything better to do? Why not pick the best thing possible that you could do? Because you're more powerful than you think, way more powerful than you think. I mean, God only knows what you are in the final analysis. You're blind to your own weaknesses, but you're also blind to your own strengths. How far could you take that if you stopped wasting time, and if you stopped lying, and if you oriented yourself to the highest possible good that you could conceive of and you committed to that? How much good could you do? Well, I would say: why don't you find out?"

SIZE
A high-resolution print size of 6' wide and 3' tall should provide ample space for both the quote and the accompanying artwork.

TYPOGRAPHY
Choose a bold, clean, and easily readable font for the quote. You could also experiment with different font sizes for certain words or phrases to emphasize their importance within the quote.

COLORS
Since the quote is thought-provoking and reflective, you might want to use a color palette that evokes a sense of introspection and depth. Consider using cool, calming colors like shades of blue, gray, or green. Alternatively, you can use a contrasting color scheme with a light background and dark text to make the quote stand out.

ARTWORK
Select / create / edit background artwork to complement the quote.
While a great design might be minimalistic and/or greyscale, I'd really like to see some full color options. This might be anything from photography or graphics inspired by the ideas in the text, to abstract colors or illustrations that feel like the sentiment expressed.
The art should capture your attention and encourage you to read the text. The art should be visually appealing, both at a distance and up close, regardless of whether the text is read.
Updates

Having trouble confirming the exact print size.

Still looking for printing solution and final size confirmation.

Target Market(s)

Personal, business, office

Industry/Entity Type

None

Font styles to use
Sans Serif
Script

Requirements
Must have
• Entire quote, legible text, modern design, attractive artwork, approx 6ft wide and 3ft tall
Nice to have
• Different font (sizes) for certain words or phrases to emphasize their importance within the quote.

```html
<!DOCTYPE html>
<html lang="en">
<head>
<meta charset="utf-8">
<title>Why Don't You Find Out — Quote Print</title>
<link rel="stylesheet" href="https://fonts.googleapis.com/css2?family=Inter:wght@700;800&family=Montserrat:wght@400;700&family=Fira+Sans:wght@400&family=Open+Sans:wght@400&family=Roboto:wght@500;700&family=Oswald:wght@700&family=Roboto+Condensed:wght@700&display=swap">
<style>
  :root {
    --ink: #333333;
    --paper: #ffffff;
    --edge: #555555;
  }
  * { margin: 0; padding: 0; box-sizing: border-box; }
  html, body { width: 1200px; height: 801px; overflow: hidden; background: var(--paper); }
  .print {
    position: relative;
    width: 1200px; height: 801px;
    border: 1px solid var(--edge);
    background: var(--paper);
    color: var(--ink);
    font-family: "Montserrat", sans-serif;
  }
  .frame { position: absolute; inset: 0; }
  .quote-line {
    position: absolute;
    left: 125px;
    height: 40px;
    line-height: 40px;
    white-space: nowrap;
  }
  .caps { font-family: "Inter", sans-serif; font-weight: 800; font-size: 23px; letter-spacing: -0.2px; }
  .bold-small { font-family: "Inter", sans-serif; font-weight: 700; font-size: 21px; }
  .reg { font-family: "Open Sans", sans-serif; font-size: 22px; }
  .soft { font-family: "Montserrat", sans-serif; font-size: 21px; }
  .mid { font-family: "Montserrat", sans-serif; font-size: 28px; }
  .large { font-family: "Montserrat", sans-serif; font-size: 32px; }
  .humanist { font-family: "Fira Sans", sans-serif; font-size: 30px; }
  .open-large { font-family: "Open Sans", sans-serif; font-size: 29px; }
  .heavy { font-family: "Montserrat", sans-serif; font-weight: 700; font-size: 30px; }
  .punch { font-family: "Inter", sans-serif; font-weight: 700; font-size: 33px; letter-spacing: -0.5px; }
  .alive {
    position: absolute;
    left: 838px; top: 104px;
    font-family: "Roboto Condensed", sans-serif;
    font-weight: 700;
    font-size: 74px;
    line-height: 74px;
    letter-spacing: 1px;
  }
  .closing {
    position: absolute;
    left: 0; width: 1200px;
    top: 640px;
    height: 46px;
    line-height: 46px;
    text-align: center;
    white-space: nowrap;
    padding-right: 60px;
  }
  .closing-lead { font-family: "Roboto", sans-serif; font-weight: 700; font-size: 35px; }
  .closing-call { font-family: "Oswald", sans-serif; font-weight: 700; font-size: 38px; margin-left: 12px; }
</style>
</head>
<body>
<main class="print">
  <svg class="frame" width="1200" height="801" viewBox="0 0 1200 801" aria-hidden="true">
    <g fill="#333333">
      <rect x="120" y="75" width="1004" height="8"/>
      <rect x="1116" y="75" width="8" height="648"/>
      <rect x="78" y="120" width="8" height="606"/>
      <rect x="78" y="718" width="1000" height="8"/>
      <!-- opening mark -->
      <path d="M46 100 L46 72 Q46 52 62 45 L66 52 Q57 58 57 70 L66 70 L66 100 Z"/>
      <path d="M78 100 L78 72 Q78 52 94 45 L98 52 Q89 58 89 70 L98 70 L98 100 Z"/>
      <!-- closing mark -->
      <path d="M1090 688 L1110 688 L1110 716 Q1110 736 1094 743 L1090 736 Q1099 730 1099 718 L1090 718 Z"/>
      <path d="M1122 688 L1142 688 L1142 716 Q1142 736 1126 743 L1122 736 Q1131 730 1131 718 L1122 718 Z"/>
    </g>
  </svg>

  <div class="quote-line" style="top:104px"><span class="caps">THE THING THAT'S SO INTERESTING ABOUT BEING</span></div>
  <div class="alive">ALIVE</div>
  <div class="quote-line" style="top:145px"><span class="bold-small">is that you're all in. No matter what you do,you're all in.</span></div>
  <div class="quote-line" style="top:186px"><span class="reg">This is gonna kill you, so I think you might as well play the most magnificent</span></div>
  <div class="quote-line" style="top:225px"><span class="soft">game you can,</span><span class="mid">while you're waiting</span><span class="soft">. Because, </span><span class="heavy">do you have</span></div>
  <div class="quote-line" style="top:265px"><span class="heavy">anything better to do? </span><span class="humanist">Why not pick the best thing possible</span></div>
  <div class="quote-line" style="top:305px"><span class="open-large">that you could do? </span><span class="reg">Because you're more powerful than you think,</span></div>
  <div class="quote-line" style="top:344px"><span class="heavy">way more powerful than you think</span><span class="soft">. I mean, God only knows</span></div>
  <div class="quote-line" style="top:383px"><span class="soft">what you are in the </span><span class="heavy">Final Analysis</span><span class="large">. You're blind to your</span></div>
  <div class="quote-line" style="top:424px"><span class="large">own weaknesses</span><span class="mid">, but you're also blind to your own</span></div>
  <div class="quote-line" style="top:464px"><span class="mid">strengths.</span><span class="soft"> How far could you take that if you </span><span class="mid">stopped wasting</span></div>
  <div class="quote-line" style="top:504px"><span class="mid">time</span><span class="soft">, and if you </span><span class="mid">stopped lying</span><span class="soft">, and if you oriented yourself to </span><span class="mid">the</span></div>
  <div class="quote-line" style="top:545px"><span class="mid">highest possible good</span><span class="soft"> that you could conceive of and </span><span class="mid">you</span></div>
  <div class="quote-line" style="top:585px"><span class="mid">committed to that</span><span class="soft">? </span><span class="punch">How much good could you do?</span></div>
  <div class="closing"><span class="closing-lead">Well, I would say:</span><span class="closing-call">WHY DON'T YOU FIND OUT?</span></div>
</main>
</body>
</html>
```